" Sou médica dermatologista com atuação na área de doenças de pele, cabelo, unhas e tratamentos estéticos como toxina botulinica, preenchimentos faciais e tratamentos para flacidez. "

```html
<!DOCTYPE html>
<html lang="pt-BR">
<head>
<meta charset="UTF-8">
<title>Pele sensível x Pele ressecada</title>
<link rel="stylesheet" href="https://fonts.googleapis.com/css2?family=Archivo:wght@400;700;800&family=Arimo:wght@400&display=swap">
<style>
  :root {
    --bg: #ebe2e0;
    --ink: #383232;
    --body: #5b504e;
    --line: #6a5f5c;
    --wave-dark: #6c605d;
    --wave-mid: #9b8f8b;
    --brand: #c8a86c;
  }
  * { margin: 0; padding: 0; box-sizing: border-box; }
  html, body { width: 1200px; height: 1200px; overflow: hidden; }
  body { background: var(--bg); font-family: "Archivo", Arial, sans-serif; }
  .post { position: relative; width: 1200px; height: 1200px; background: var(--bg); overflow: hidden; }
  .frame-line { position: absolute; background: var(--line); }
  .frame-line--top { left: 93px; top: 93px; width: 420px; height: 2px; }
  .frame-line--side { left: 93px; top: 93px; width: 2px; height: 520px; }
  .title {
    position: absolute; top: 222px;
    font-weight: 800; font-size: 63px; line-height: 0.98;
    color: var(--ink); letter-spacing: -0.5px; text-transform: uppercase;
  }
  .title--sensitive { left: 243px; }
  .title--dry { left: 724px; }
  .skin-photo { position: absolute; top: 437px; width: 326px; height: 326px; border-radius: 50%; border: 3px solid #f4eeec; }
  .skin-photo--sensitive { left: 100px; background: radial-gradient(circle at 55% 35%, #c94a58 0%, #d98580 35%, #e3b09e 70%, #d9a890 100%); }
  .skin-photo--dry { left: 691px; background: radial-gradient(circle at 50% 50%, #e8b89c 0%, #dca588 55%, #cf9679 100%); }
  .versus {
    position: absolute; left: 548px; top: 530px; width: 120px; text-align: center;
    font-family: "Arimo", Arial, sans-serif; font-weight: 400; font-size: 128px; line-height: 1; color: var(--ink);
  }
  .body-copy {
    position: absolute; left: 244px; top: 848px; width: 740px;
    font-family: "Arimo", Arial, sans-serif; font-size: 26.5px; line-height: 35px; color: var(--body);
  }
  .wave { position: absolute; left: 0; bottom: 0; width: 1200px; height: 260px; }
  .brand {
    position: absolute; right: 70px; bottom: 70px;
    display: flex; align-items: center; gap: 14px;
    font-family: "Archivo", Arial, sans-serif; font-weight: 700; font-size: 34px; color: var(--brand);
  }
  .brand__dot { width: 18px; height: 18px; border-radius: 50%; background: var(--brand); }
</style>
</head>
<body>
  <main class="post">
    <div class="frame-line frame-line--top"></div>
    <div class="frame-line frame-line--side"></div>

    <h2 class="title title--sensitive">Pele<br>Sensível</h2>
    <h2 class="title title--dry">Pele<br>Ressecada</h2>

    <div class="skin-photo skin-photo--sensitive" role="img" aria-label="Foto em close de pele sensível com vermelhidão na bochecha"></div>
    <div class="versus">X</div>
    <div class="skin-photo skin-photo--dry" role="img" aria-label="Foto em close de pele ressecada com textura descamada"></div>

    <p class="body-copy">Lorem ipsum dolor sit amet, consectetur adipiscing elit, sed do eiusmod tempor incididunt ut labore et dolore magna aliqua. Quis ipsum suspendisse ultrices gravida. Risus commodo viverra maecenas accumsan lacus vel facilisis.</p>

    <svg class="wave" viewBox="0 0 1200 260" preserveAspectRatio="none" aria-hidden="true">
      <path d="M0,230 C320,215 560,180 760,110 C900,62 1060,70 1200,120 L1200,260 L0,260 Z" fill="var(--wave-mid)" opacity="0.55"/>
      <path d="M0,250 C330,240 580,205 790,135 C930,90 1070,100 1200,145 L1200,260 L0,260 Z" fill="var(--wave-dark)"/>
    </svg>

    <div class="brand"><span class="brand__dot"></span>Dra. Lívia Mattos</div>
  </main>
</body>
</html>
```